Redesign of corporate card

We need a double sided card designed to use for all our REALTORS. We are a real estate Brokerage firm in Ottawa, Ontario Canada. Our cards will have our logo on them. The information on the card for is one is as follows: Donna Hartlyn, Broker. Kestmoor Realty, Brokerage. (613) 555-0147 Ext 3. dhartlyn@kestmoor-example.ca. www.donnahartlyn-example.ca. Attached is our logo, agent picture.

Most of the back should be used for a note.

We have included a proof of our sign. Should have some of the characteristics of the sign.

Reason: I have asked for changes several times but as of now the changes have not been made, nor has there been a reply. The design # is : 7384916 and I want a watermark on the side with the persons picture that is on the notes side or right side of the card. There is one on the other side and it should be somewhat similar. I am speaking of the stylized K.

Target Market(s)

prospective buyers and sellers, past clients, other Realtors

Industry/Entity Type

Real Estate

Other font styles liked:
• Tragen

Requirements
Must have
• Beside the agents name their designation must be either beside or under. Can be smaller: Donna Hartlyn, Broker
The brokerage name Kestmoor Realty, must have the word Brokerage beside or under, can be smaller: Kestmoor Realty, Brokerage

```html
<!DOCTYPE html>
<html lang="en">
<head>
<meta charset="utf-8">
<title>Donna Hartlyn – Kestmoor Realty Business Card</title>
<link rel="stylesheet" href="https://fonts.googleapis.com/css2?family=Cinzel:wght@400;600&family=EB+Garamond:wght@400;500&display=swap">
<style>
  :root {
    --card-blue: #4a88bb;
    --card-blue-deep: #3f79a8;
    --ink: #111418;
    --paper: #ffffff;
    --stage: #e9ecef;
    --photo-dark: #1f2123;
    --photo-mid: #3a3b3c;
  }
  * { margin: 0; padding: 0; box-sizing: border-box; }
  html, body { width: 1200px; height: 960px; overflow: hidden; }
  body {
    background: var(--stage);
    display: flex;
    flex-direction: column;
    align-items: center;
    justify-content: center;
    gap: 50px;
  }
  .card {
    position: relative;
    width: 700px;
    height: 400px;
    background: var(--card-blue);
    border-radius: 22px;
    box-shadow: 0 10px 24px rgba(30, 50, 70, 0.22);
    overflow: hidden;
  }

  /* Front side */
  .photo-frame {
    position: absolute;
    left: 22px;
    top: 100px;
    width: 330px;
    height: 278px;
    background: var(--paper);
    padding: 12px;
  }
  .photo-area {
    width: 100%;
    height: 100%;
    background: radial-gradient(circle at 45% 45%, var(--photo-mid), var(--photo-dark) 70%);
  }
  .agent-name {
    position: absolute;
    left: 372px;
    top: 40px;
    font-family: "Cinzel", serif;
    font-weight: 400;
    font-size: 34px;
    letter-spacing: 1px;
    color: var(--paper);
    line-height: 1;
  }
  .agent-title {
    position: absolute;
    left: 392px;
    top: 82px;
    font-family: "EB Garamond", serif;
    font-weight: 500;
    font-size: 15px;
    color: var(--ink);
  }
  .contact-list {
    position: absolute;
    left: 392px;
    top: 185px;
    list-style: none;
    font-family: "EB Garamond", serif;
    font-weight: 500;
    font-size: 19px;
    color: var(--ink);
  }
  .contact-list li {
    display: flex;
    align-items: flex-start;
    gap: 16px;
    margin-bottom: 12px;
    line-height: 1.15;
  }
  .contact-list svg { flex: 0 0 auto; margin-top: 2px; }
  .ext { display: block; padding-left: 18px; }

  /* Back side */
  .brand {
    position: absolute;
    left: 0;
    right: 0;
    top: 150px;
    display: flex;
    align-items: center;
    justify-content: center;
    gap: 16px;
    font-family: "Cinzel", serif;
    font-weight: 400;
    font-size: 44px;
    color: var(--paper);
    letter-spacing: 2px;
  }
  .brand-dot {
    width: 18px;
    height: 18px;
    border-radius: 50%;
    background: var(--paper);
  }
  .brokerage-line {
    position: absolute;
    left: 0;
    right: 0;
    bottom: 54px;
    text-align: center;
    font-family: "Cinzel", serif;
    font-weight: 400;
    font-size: 22px;
    letter-spacing: 1px;
    color: var(--paper);
  }
  .brokerage-line .divider { margin: 0 14px; }
</style>
</head>
<body>

  <section class="card card-front">
    <div class="photo-frame">
      <div class="photo-area" role="img" aria-label="Portrait photograph of agent Donna Hartlyn on a dark background"></div>
    </div>
    <h1 class="agent-name">Donna Hartlyn</h1>
    <p class="agent-title">Broker</p>
    <ul class="contact-list">
      <li>
        <svg width="16" height="16" viewBox="0 0 24 24" aria-hidden="true"><path fill="#fff" d="M6.6 10.8c1.4 2.8 3.8 5.1 6.6 6.6l2.2-2.2c.3-.3.7-.4 1-.2 1.1.4 2.3.6 3.6.6.6 0 1 .4 1 1V20c0 .6-.4 1-1 1C10.6 21 3 13.4 3 4c0-.6.4-1 1-1h3.5c.6 0 1 .4 1 1 0 1.3.2 2.5.6 3.6.1.3 0 .7-.2 1z"/></svg>
        <span>(613) 555-0147<span class="ext">( Ext 3 )</span></span>
      </li>
      <li>
        <svg width="16" height="16" viewBox="0 0 24 24" aria-hidden="true"><rect x="2" y="5" width="20" height="14" fill="#fff"/><path d="M2 5l10 8 10-8" fill="none" stroke="#4a88bb" stroke-width="1.6"/></svg>
        <span>dhartlyn@kestmoor-example.ca</span>
      </li>
      <li>
        <svg width="16" height="16" viewBox="0 0 24 24" aria-hidden="true"><circle cx="12" cy="12" r="10" fill="#fff"/><path d="M2 12h20M12 2c3 3 3 17 0 20M12 2c-3 3-3 17 0 20" fill="none" stroke="#4a88bb" stroke-width="1.4"/></svg>
        <span>www.donnahartlyn-example.ca</span>
      </li>
    </ul>
  </section>

  <section class="card card-back">
    <div class="brand">
      <span class="brand-dot" aria-hidden="true"></span>
      <span class="brand-name">Kestmoor Realty</span>
    </div>
    <p class="brokerage-line">Kestmoor Realty<span class="divider">/</span>Brokerage</p>
  </section>

</body>
</html>
```